Design a label for a range of honey under :BRIGHT MEADOW HONEY. (Original quirky different)

Create a label for a range of honey products under the brand BRIGHT MEADOW HONEY.
Iam the beekeeper and want to sell for the local New Zealand market directly to the consumer, online mainly.
Brand position: A contemporary honey, a fresh look for a simple product, like nature intended, nothing taken out, nothing added. Doesnt take itself seriously.
Personality: Contemporary, fresh, modern, free and fun,loving. Doesnt take itself seriously, loving, generous, upbeat, provide enjoyment, life ...
Brand value: Straight up, keep it simple, generous, different,
Label: Modern twist of nature and goodness (no straight picture of nature) quirky?, use of slogan? ( Nature in a pot / Simply honey / Taste of nature / It's all good...
Need to stand out, make you smile, be noticed, different...

Target Market(s)

Online direct customer.

Requirements
Must have
• legal requirements for NZ labeling attached.
A twist and quirky side...
Should not have
• Basic picture of nature.
Straight forward boring everybody else's feel.

```html
<!DOCTYPE html>
<html lang="en">
<head>
<meta charset="utf-8">
<title>Bright Meadow Honey – Jar Label</title>
<link rel="stylesheet" href="https://fonts.googleapis.com/css2?family=Lato:wght@400;700&family=Mulish:wght@600;700&display=swap">
<style>
  :root {
    --backdrop: #e9e9eb;
    --label-white: #ffffff;
    --ink: #111111;
    --honey-light: #f0cf00;
    --honey-mid: #e2bb00;
    --honey-deep: #d2a300;
    --gold-edge: #c99a00;
  }
  html, body {
    margin: 0;
    padding: 0;
    width: 1200px;
    height: 995px;
    overflow: hidden;
    background: var(--backdrop);
  }
  .canvas {
    position: relative;
    width: 1200px;
    height: 995px;
    display: flex;
    align-items: center;
    justify-content: center;
  }
  .jar-label {
    width: 600px;
    height: 769px;
    display: block;
    box-shadow: 0 2px 10px rgba(0,0,0,0.08);
  }
  .label-small {
    font-family: "Lato", Arial, sans-serif;
    fill: var(--ink);
  }
  .label-title {
    font-family: "Mulish", "Lato", Arial, sans-serif;
    font-weight: 700;
    fill: var(--ink);
  }
</style>
</head>
<body>
<main class="canvas">
  <svg class="jar-label" viewBox="0 0 320 410" xmlns="http://www.w3.org/2000/svg" role="img" aria-label="Bright Meadow honey jar label: Simply Sunny, 100% natural Raw, NetWt 17 oz">
    <defs>
      <linearGradient id="honey-fill" x1="0" y1="0" x2="1" y2="1">
        <stop offset="0" stop-color="var(--honey-light)"/>
        <stop offset="0.55" stop-color="var(--honey-mid)"/>
        <stop offset="1" stop-color="var(--honey-deep)"/>
      </linearGradient>
    </defs>

    <rect class="label-base" x="0" y="0" width="320" height="410" rx="6" fill="var(--label-white)"/>
    <rect class="label-band" x="0" y="58" width="320" height="110" fill="var(--ink)"/>

    <polygon class="hex-frame" points="3,204 62,37 258,37 317,204 258,372 62,372"
             fill="var(--ink)" stroke="var(--gold-edge)" stroke-width="1.6" stroke-linejoin="round"/>
    <polygon class="hex-panel" points="26,204 76,58 244,58 294,204 244,351 76,351"
             fill="url(#honey-fill)" stroke="var(--gold-edge)" stroke-width="1.2" stroke-linejoin="round"/>

    <text class="label-small est" x="160" y="81" text-anchor="middle" font-size="7" letter-spacing="1.6">EST . 2020</text>
    <circle class="brand-dot" cx="160" cy="105" r="9" fill="none" stroke="var(--ink)" stroke-width="1.2"/>
    <text class="label-small brand-name" x="160" y="145" text-anchor="middle" font-size="10" letter-spacing="0.3">BRIGHT MEADOW</text>
    <line class="rule" x1="118" y1="156" x2="202" y2="156" stroke="var(--ink)" stroke-width="1.4"/>

    <text class="label-small slogan" x="160" y="181" text-anchor="middle" font-size="13.5">Simply</text>
    <text class="label-title product-name" x="160" y="233" text-anchor="middle" font-size="52" letter-spacing="-1">Sunny</text>
    <line class="rule" x1="118" y1="253" x2="202" y2="253" stroke="var(--ink)" stroke-width="1.4"/>

    <text class="label-small claim" x="160" y="281" text-anchor="middle" font-size="12.5">100% natural Raw</text>
    <text class="label-small net-weight" x="160" y="330" text-anchor="middle" font-size="9.5">NetWt: 17 oz</text>
  </svg>
</main>
</body>
</html>
```